A5 Flyer for Financial Services Business

I am after a re-design of our business flyer to fit in with our new branding style and logo colour scheme. Wanting something with a bit of designer flair that I could not create myself. I have included the flyer which I created which lacks style so dazzle me.

I want to use the same content.

Text for main body of flyer is

Are you a small business owner, tradie or PAVC Service Provider struggling to stay on top of your bookkeeping and compliance obligations? If so we would love to help you get back on track and take control of your business finances so that you can make informed business decisions and focus on what you do best.

We have over 20 years industry experience and, as a small business ourselves, we are able to offer our clients a personal bookkeeping solution tailored to meet the needs of your business.

Accounts Payable | Accounts Receivable
Customer Invoicing
Bank and Credit Card Reconciliations
Payroll | Superannuation | Payroll Tax
Business Activity | Instalment Activity Statements
Regular Financial Reports
Cloudbooks and Ledgerline Set-Up and Training

```html
<!DOCTYPE html>
<html lang="en">
<head>
<meta charset="utf-8">
<title>Even Ledger Financial Services – Bookkeeping Flyer</title>
<link rel="stylesheet" href="https://fonts.googleapis.com/css2?family=Open+Sans:wght@400;600;700;800&display=swap">
<style>
  :root {
    --teal: #067d89;
    --teal-bright: #0a9ea3;
    --navy: #0b2f48;
    --ink: #0a0a0a;
    --body-grey: #666a6e;
    --paper: #ffffff;
    --backdrop: #e9e9e9;
    --silver: #b9bcc0;
  }
  * { margin: 0; padding: 0; box-sizing: border-box; }
  html, body { width: 1200px; height: 1067px; overflow: hidden; background: var(--backdrop); }
  body { font-family: "Open Sans", sans-serif; position: relative; }

  .flyer {
    position: absolute;
    left: 248px; top: 33px;
    width: 913px; height: 1295px;
    background: var(--paper);
    transform: scale(0.7722);
    transform-origin: top left;
    overflow: hidden;
  }
  .flyer-shapes { position: absolute; inset: 0; }

  .brand {
    position: absolute; left: 30px; top: 60px;
    display: flex; align-items: center; gap: 10px;
  }
  .brand-dot { width: 26px; height: 26px; border-radius: 50%; background: var(--teal); }
  .brand-name {
    font-family: "Open Sans", sans-serif; font-weight: 700;
    font-size: 25px; line-height: 1.15; color: var(--teal); letter-spacing: 0.5px;
  }

  .headline {
    position: absolute; left: 40px; top: 430px; width: 460px;
    font-weight: 800; font-size: 52px; line-height: 59px;
    letter-spacing: 2px; color: var(--ink); text-transform: uppercase;
    white-space: nowrap;
  }
  .headline .accent { color: var(--teal); }
  .headline-rule { position: absolute; left: 45px; top: 702px; width: 39px; height: 12px; background: var(--teal); }

  .intro {
    position: absolute; left: 45px; width: 444px;
    font-size: 17px; line-height: 24px; letter-spacing: 0.6px;
    color: var(--body-grey); text-align: justify;
  }
  .intro-first { top: 731px; }
  .intro-second { top: 923px; }

  .services { list-style: none; position: absolute; left: 0; top: 0; }
  .service {
    position: absolute; left: 539px; width: 330px;
    display: flex; gap: 19px;
    font-weight: 600; font-size: 23.5px; line-height: 26px;
    letter-spacing: 1.4px; color: var(--paper); white-space: nowrap;
  }
  .service svg { flex: none; margin-top: 4px; }

  .contact { position: absolute; left: 0; top: 0; color: var(--paper); }
  .contact-label { position: absolute; left: 108px; top: 1142px; font-weight: 800; font-size: 28px; letter-spacing: 1.5px; white-space: nowrap; }
  .contact-phone { position: absolute; left: 106px; top: 1172px; font-weight: 700; font-size: 52px; letter-spacing: 3px; white-space: nowrap; }
  .contact-web { position: absolute; left: 113px; top: 1234px; font-weight: 400; font-size: 30px; letter-spacing: 1.5px; white-space: nowrap; }
  .contact-icon { position: absolute; left: 54px; }
</style>
</head>
<body>
  <div class="flyer">
    <svg class="flyer-shapes" width="913" height="1295" viewBox="0 0 913 1295">
      <defs>
        <linearGradient id="photoTone" x1="0" y1="0" x2="1" y2="1">
          <stop offset="0" stop-color="#d9ddd8"/>
          <stop offset="0.45" stop-color="#c9cfc6"/>
          <stop offset="0.7" stop-color="#e6e4e6"/>
          <stop offset="1" stop-color="#cbb59c"/>
        </linearGradient>
        <linearGradient id="stripeTone" x1="0" y1="0" x2="1" y2="0">
          <stop offset="0" stop-color="#0aa6a6"/>
          <stop offset="0.6" stop-color="#067d89"/>
          <stop offset="1" stop-color="#0b2f48"/>
        </linearGradient>
        <linearGradient id="silverTone" x1="0" y1="0" x2="1" y2="0">
          <stop offset="0" stop-color="#f4f4f5"/>
          <stop offset="1" stop-color="#8e9196"/>
        </linearGradient>
        <linearGradient id="cornerTone" x1="0" y1="0" x2="1" y2="0">
          <stop offset="0" stop-color="#0a9ea3"/>
          <stop offset="0.55" stop-color="#075f73"/>
          <stop offset="1" stop-color="#0b2a40"/>
        </linearGradient>
      </defs>

      <polygon points="0,0 913,0 913,430 0,308" fill="url(#photoTone)" role="img" aria-label="Photo of a bookkeeper working with papers and a calculator at a desk"/>
      <polygon points="0,0 460,0 180,226 0,135" fill="var(--paper)"/>

      <polygon points="0,355 913,470 913,480 0,325" fill="#eceef0"/>
      <polygon points="0,305 913,428 913,480 0,318" fill="url(#stripeTone)"/>
      <polygon points="0,318 913,470 913,480 0,330" fill="url(#silverTone)"/>

      <polygon points="240,1100 913,940 913,1170 240,1170" fill="#f3f4f5"/>
      <polygon points="0,1078 913,1168 913,1200 0,1107" fill="url(#silverTone)"/>
      <polygon points="0,1107 913,1200 913,1295 0,1295" fill="var(--teal)"/>

      <polygon points="520,470 872,512 872,1130 520,1130" fill="var(--teal)"/>
      <polygon points="519,1130 913,1049 913,1170" fill="url(#cornerTone)"/>
    </svg>

    <div class="brand">
      <span class="brand-dot"></span>
      <span class="brand-name">EVEN LEDGER<br>Financial Services</span>
    </div>

    <h1 class="headline">
      <span class="accent">Bookkeeping<br>tailored to</span><br>your business<br>needs
    </h1>
    <div class="headline-rule"></div>

    <p class="intro intro-first">Are you a small business owner, tradie or PAVC Service Provider struggling to stay on top of your bookkeeping and compliance obligations? If so we would love to help you get back on track and take control of your business finances so that you can make informed business decisions and focus on what you do best.</p>
    <p class="intro intro-second">We have over 20 years industry experience and, as a small business ourselves, we are able to offer our clients a personal bookkeeping solution tailored to meet the needs of your business.</p>

    <ul class="services">
      <li class="service" style="top:536px"><svg width="20" height="20" viewBox="0 0 20 20"><circle cx="10" cy="10" r="10" fill="#fff"/><path d="M5.5 10.3l3 3 6-6.2" fill="none" stroke="var(--teal)" stroke-width="2.4"/></svg><span>Accounts Payable |<br>Accounts Receivable</span></li>
      <li class="service" style="top:608px"><svg width="20" height="20" viewBox="0 0 20 20"><circle cx="10" cy="10" r="10" fill="#fff"/><path d="M5.5 10.3l3 3 6-6.2" fill="none" stroke="var(--teal)" stroke-width="2.4"/></svg><span>Customer Invoicing</span></li>
      <li class="service" style="top:654px"><svg width="20" height="20" viewBox="0 0 20 20"><circle cx="10" cy="10" r="10" fill="#fff"/><path d="M5.5 10.3l3 3 6-6.2" fill="none" stroke="var(--teal)" stroke-width="2.4"/></svg><span>Bank and Credit<br>Card Reconciliations</span></li>
      <li class="service" style="top:727px"><svg width="20" height="20" viewBox="0 0 20 20"><circle cx="10" cy="10" r="10" fill="#fff"/><path d="M5.5 10.3l3 3 6-6.2" fill="none" stroke="var(--teal)" stroke-width="2.4"/></svg><span>Payroll |<br>Superannuation |<br>Payroll Tax</span></li>
      <li class="service" style="top:821px"><svg width="20" height="20" viewBox="0 0 20 20"><circle cx="10" cy="10" r="10" fill="#fff"/><path d="M5.5 10.3l3 3 6-6.2" fill="none" stroke="var(--teal)" stroke-width="2.4"/></svg><span>Business Activity |<br>Instalment Activity<br>Statements</span></li>
      <li class="service" style="top:913px"><svg width="20" height="20" viewBox="0 0 20 20"><circle cx="10" cy="10" r="10" fill="#fff"/><path d="M5.5 10.3l3 3 6-6.2" fill="none" stroke="var(--teal)" stroke-width="2.4"/></svg><span>Regular Financial<br>Reports</span></li>
      <li class="service" style="top:983px"><svg width="20" height="20" viewBox="0 0 20 20"><circle cx="10" cy="10" r="10" fill="#fff"/><path d="M5.5 10.3l3 3 6-6.2" fill="none" stroke="var(--teal)" stroke-width="2.4"/></svg><span>Cloudbooks and<br>Ledgerline Set-Up<br>and Training</span></li>
    </ul>

    <div class="contact">
      <div class="contact-label">Contact Us</div>
      <svg class="contact-icon" style="top:1192px" width="32" height="32" viewBox="0 0 32 32">
        <circle cx="16" cy="16" r="16" fill="#fff"/>
        <path d="M11 8.5l3 3.2-1.6 2c1.2 2.4 3 4.3 5.6 5.6l2-1.6 3.2 3-1.8 2.6c-6.4-.8-11.3-5.8-12-12z" fill="var(--teal)"/>
      </svg>
      <div class="contact-phone">0400 123 987</div>
      <svg class="contact-icon" style="top:1243px" width="32" height="32" viewBox="0 0 32 32">
        <circle cx="16" cy="16" r="16" fill="#fff"/>
        <g fill="none" stroke="var(--teal)" stroke-width="1.6">
          <circle cx="16" cy="16" r="10"/>
          <ellipse cx="16" cy="16" rx="4.5" ry="10"/>
          <path d="M6 16h20M8 11h16M8 21h16"/>
        </g>
      </svg>
      <div class="contact-web">www.evenledgerfinancial.com.au</div>
    </div>
  </div>
</body>
</html>
```